Business Card Design

I am a cosmetic tattooist in Melbourne Australia, who provides services where by I tattoo eyebrows in block or strokes with a tattooing gun. Feathering that mimic hair strands with a scalpel. Eyeliner top and bottom with the tattooing gun. Lips just as either an outline or a full block colour where the top and bottom lip is completely covered. Corrections for tattooing done previously that have either faded to quickly, turned blue or orange due to bad colour choice, or a mishap. Paramedical colouring for people who either have scaring that needs to be matched to their skin colour. Patients who have alopecia or a skin condition that needs hair like tattooing. Cancer patients who's nipples and areolas have been partially or totally been removed and require them to be re drawn into the new skin. I colour match with a variety of inks (around 50) at my disposal and can also lift colours with a pigmentation lifter. I also require the use of two different types of anaesthetics throughout each procedure.
Colours that I have looked into the represent health, professionalism, beauty, skin and medical type procedures are Light to dark brown, Light to dark grey, Black and White. Possibly a splash of red to represent the lips. I am mobile and can work from any venue that takes a commission for a bed. I have completed a diploma in cosmetic tattooing being qualified.
Updates

Project Deadline Extended
Reason: I have been awaiting for a design from own more designer who accepted my project but hasn't released their design.

Project Deadline Extended

Industry/Entity Type

Medical

Contact Information for Business Card

Company name: Velvet Arch Cosmetic Tattooing
Name: Lorna Beswick
Title: Cosmetic and Paramedical Tattooist
Address: P.O Box 2863, Ashmont Heights, Victoria 3297
Mobile: 0417365821
Email: velvetarchtattooing@quillmail.example
Preferred colours: Light brown, Light Grey, Black (writing) White Background

Requirements
Nice to have
• A shape of the eyebrow or eye with eyeliner in the background. Possibly red lips. No straight lines, only curved or curled lines.

```html
<!DOCTYPE html>
<html lang="en">
<head>
<meta charset="utf-8">
<title>Velvet Arch Cosmetic Tattooing – Business Card</title>
<link rel="stylesheet" href="https://fonts.googleapis.com/css2?family=Open+Sans:wght@400;600;700&family=Arimo:wght@400&display=swap">
<style>
  :root {
    --backdrop: #e9e6e2;
    --card: #ffffff;
    --brand-red: #9e1c22;
    --ink: #111111;
    --ink-soft: #2a2a2a;
    --eye-dark: #3a3a3a;
    --eye-mid: #9a9a9a;
    --eye-light: #d9d9d9;
  }
  * { box-sizing: border-box; margin: 0; padding: 0; }
  html, body {
    width: 1200px; height: 1200px; overflow: hidden;
    background: var(--backdrop);
  }
  .canvas {
    position: relative; width: 1200px; height: 1200px;
    display: flex; align-items: center; justify-content: center;
  }
  .business-card {
    position: relative; width: 1050px; height: 600px;
    background: var(--card);
    box-shadow: 0 10px 30px rgba(0,0,0,0.18);
    overflow: hidden;
  }
  .eye-photo {
    position: absolute; right: 0; top: 0;
    width: 560px; height: 500px;
    background:
      radial-gradient(ellipse 38% 22% at 52% 52%, var(--eye-dark) 0%, var(--eye-mid) 55%, transparent 100%),
      radial-gradient(ellipse 60% 42% at 58% 34%, var(--eye-light) 0%, var(--eye-mid) 45%, rgba(255,255,255,0) 100%),
      linear-gradient(to left, rgba(255,255,255,0) 60%, var(--card) 100%);
    -webkit-mask-image: radial-gradient(ellipse 70% 60% at 60% 42%, #000 55%, transparent 100%);
    mask-image: radial-gradient(ellipse 70% 60% at 60% 42%, #000 55%, transparent 100%);
  }
  .brand-name {
    position: absolute; left: 56px; top: 36px;
    font-family: "Open Sans", sans-serif; font-weight: 600;
    font-size: 42px; line-height: 1.15;
    color: var(--brand-red);
  }
  .brand-name .line-two { display: block; padding-left: 120px; }
  .holder {
    position: absolute; left: 60px; top: 232px;
  }
  .holder-name {
    font-family: "Open Sans", sans-serif; font-weight: 700;
    font-size: 40px; color: var(--ink);
  }
  .holder-title {
    font-family: "Open Sans", sans-serif; font-weight: 400;
    font-size: 24px; color: var(--ink-soft); margin-top: 2px;
  }
  .contact-list {
    position: absolute; left: 60px; top: 372px;
    list-style: none;
    font-family: "Arimo", sans-serif; font-size: 27px;
    line-height: 48px; color: var(--ink);
  }
</style>
</head>
<body>
  <main class="canvas">
    <section class="business-card">
      <div class="eye-photo" role="img" aria-label="Close-up photograph of a made-up eye with long dark lashes and silver glitter shadow"></div>
      <h1 class="brand-name">Velvet Arch Cosmetic<span class="line-two">Tattooing</span></h1>
      <div class="holder">
        <p class="holder-name">Lorna Beswick</p>
        <p class="holder-title">Cosmetic and Paramedical Tattooist</p>
      </div>
      <ul class="contact-list">
        <li>Address: P.O Box 2863, Ashmont Heights, Victoria 3297</li>
        <li>Mobile: 0417365821</li>
        <li>Email: velvetarchtattooing@quillmail.example</li>
      </ul>
    </section>
  </main>
</body>
</html>
```